Harvest Gathering event flyer

I would like a church event flyer designed. The event is called "HARVEST GATHERING 2018". I am looking for a professional, yet catchy design that uses our brand colors and logo creatively while communicating key information of the event effectively.

1. The logo is attached in two color formats. The designer has the choice to use them as he/she want.

2. The location of the event is: Lindqvist Community Center, 482 Tamsworth Street, Portland, ME 04102
3. Time and date of event. The designer can organize and format the date and time as he/she pleases.
December 28th, 29th @ 7:00PM
December 30th @ 10:00AM
4. The topic of the event is "Tongues of fire". The designer is free to use this phrase as he/she pleases to create a good composition.
5. Speaker: Prophet Marcus Obuya
6. Contact information: contact@cedarbrookfellowship.org - Telephone number: 207 555 0148

7. I would also like the following three words on the flyer. These words describe the focus of the event: FIRE, REVIVAL, PROPHETIC

```html
<!DOCTYPE html>
<html lang="en">
<head>
<meta charset="utf-8">
<title>Harvest Gathering 2018 – Tongues of Fire</title>
<link rel="stylesheet" href="https://fonts.googleapis.com/css2?family=Cinzel:wght@400;600;700&family=Damion&family=Oswald:wght@400&family=Cormorant+Garamond:wght@500;600&display=swap">
<style>
  :root{
    --backdrop:#9a9a9a;
    --navy:#1f3b5e;
    --navy-deep:#1c3557;
    --fog:#b3c0dc;
    --fog-mid:#7d90b8;
    --orange:#f39322;
    --orange-muted:#d9914a;
    --white:#ffffff;
    --info:#b6c0d4;
  }
  *{margin:0;padding:0;box-sizing:border-box}
  html,body{width:1200px;height:1200px;overflow:hidden;background:var(--backdrop)}
  .flyer{
    position:absolute;left:241px;top:91px;width:718px;height:1018px;
    background:var(--navy);overflow:hidden;
  }
  .hero-photo{
    position:absolute;inset:0 0 auto 0;height:560px;
    background:
      radial-gradient(ellipse 60% 55% at 45% 38%, var(--fog) 0%, #9dadd0 40%, var(--fog-mid) 70%, rgba(31,59,94,0) 100%),
      linear-gradient(180deg,#3d5a86 0%,#5c74a3 35%,#7286b0 60%,var(--navy) 100%);
  }
  .brand{
    position:absolute;right:58px;top:120px;
    display:flex;align-items:center;gap:10px;
    font-family:"Cormorant Garamond",serif;font-weight:600;
    font-size:40px;letter-spacing:1px;color:var(--white);
  }
  .brand-dot{width:16px;height:16px;border-radius:50%;background:var(--orange)}
  .headline{position:absolute;left:0;top:440px;width:718px;height:300px}
  .event-name{font-family:"Damion",cursive;fill:var(--white)}
  .event-year{font-family:"Cormorant Garamond",serif;font-weight:600;fill:var(--white)}
  .topic-lead{font-family:"Cinzel",serif;font-weight:400;fill:var(--orange-muted)}
  .topic-main{font-family:"Cinzel",serif;font-weight:400;fill:var(--orange)}
  .glow-line{position:absolute;left:60px;width:600px;height:2px;
    background:linear-gradient(90deg,rgba(243,147,34,0),rgba(255,190,110,.9) 50%,rgba(243,147,34,0))}
  .focus{
    position:absolute;left:0;top:738px;width:718px;text-align:center;
    font-family:"Cinzel",serif;font-weight:700;font-size:37px;letter-spacing:1px;color:var(--white);
  }
  .dates{
    position:absolute;left:0;top:806px;width:718px;text-align:center;
    font-family:"Oswald",sans-serif;font-size:25px;letter-spacing:0;color:var(--info);
    transform:scaleX(.86);
  }
  .address{
    position:absolute;left:0;top:838px;width:718px;text-align:center;
    font-family:"Cinzel",serif;font-size:22px;letter-spacing:2px;color:var(--info);
  }
  .rule{position:absolute;left:92px;width:530px;height:1px;background:var(--orange-muted)}
  .speaker{
    position:absolute;left:0;top:880px;width:718px;text-align:center;
    font-family:"Cinzel",serif;font-size:26px;letter-spacing:1.5px;color:var(--orange-muted);
  }
  .contact{
    position:absolute;left:0;top:940px;width:718px;
    display:flex;justify-content:center;align-items:center;gap:10px;
    font-family:"Cormorant Garamond",serif;font-weight:600;color:var(--white);
  }
  .contact-phone{font-size:22px}
  .contact-email{font-size:16px;letter-spacing:1px;text-transform:uppercase;font-family:"Cinzel",serif;font-weight:400}
  .contact-icon{width:24px;height:24px;flex:none}
</style>
</head>
<body>
  <main class="flyer">
    <div class="hero-photo" role="img" aria-label="Silhouette of a lone figure standing on a misty hilltop in soft blue fog"></div>

    <div class="brand"><span class="brand-dot"></span>CEDARBROOK</div>

    <svg class="headline" viewBox="0 0 718 300" aria-label="Harvest Gathering 2018 – Tongues of Fire">
      <text class="event-name" x="96" y="32" font-size="46" textLength="330" lengthAdjust="spacingAndGlyphs">Harvest Gathering</text>
      <text class="event-year" x="438" y="32" font-size="50">2018</text>
      <text class="topic-lead" x="68" y="100" font-size="90" textLength="578" lengthAdjust="spacingAndGlyphs">TONGUES OF</text>
      <text class="topic-main" x="66" y="292" font-size="262" textLength="584" lengthAdjust="spacingAndGlyphs">FIRE</text>
    </svg>

    <div class="glow-line" style="top:731px"></div>
    <p class="focus">FIRE, REVIVAL, PROPHETIC</p>
    <div class="glow-line" style="top:784px"></div>

    <p class="dates">DECEMBER 28TH, 29TH @ 7:00PM &nbsp;|&nbsp; DECEMBER 30TH @ 10:00AM</p>
    <p class="address">482 TAMSWORTH STREET, PORTLAND, ME 04102</p>

    <div class="rule" style="top:874px"></div>
    <p class="speaker">SPEAKER: PROPHET MARCUS OBUYA</p>
    <div class="rule" style="top:917px"></div>

    <div class="contact">
      <svg class="contact-icon" viewBox="0 0 24 24" aria-hidden="true">
        <circle cx="12" cy="12" r="11" fill="none" stroke="#f39322" stroke-width="1.5"/>
        <path d="M8.5 6.5l2 2.5-1.2 1.4c.7 1.6 1.9 2.8 3.4 3.5l1.4-1.2 2.4 2-1.2 1.8c-3.6-.4-7.1-3.9-7.6-7.6z" fill="#f39322"/>
      </svg>
      <span class="contact-phone">207 555 0148</span>
      <svg class="contact-icon" viewBox="0 0 24 24" aria-hidden="true" style="margin-left:6px">
        <circle cx="12" cy="12" r="11" fill="none" stroke="#f39322" stroke-width="1.5"/>
        <rect x="7" y="8.5" width="10" height="7" fill="none" stroke="#f39322" stroke-width="1.3"/>
        <path d="M7 8.5l5 4 5-4" fill="none" stroke="#f39322" stroke-width="1.3"/>
      </svg>
      <span class="contact-email">contact@cedarbrookfellowship.org</span>
    </div>
  </main>
</body>
</html>
```